Aerial photo/video drone company needs new business card

Aerial visual company who offers photos and video services via drones.

We are QVL certified and work in the real estate, insurance, construction, and film industries.

I'm looking for a clean, professional, maybe even edgy design, that will be a conversation starter when networking.

I've included our logo, current business card, and font.

Our current business card is decent; albeit, I'm looking for something more unique. If you folks provide good designs, I'll definitely guarantee payment (and I'm not opposed to tipping if the design is above and beyond).

Target Market(s)

Insurance companies, real estate agents, construction companies, advertising & other creative agencies, and filmmakers/producers.

Industry/Entity Type

Business

Contact Information for Business Card

Company name pronounced air-a-vee.

Font styles to use
Other font styles liked:
• Font was uploaded; that or similar; not opposed to other fonts if they work well with the design

Requirements
Must have
• Clearly prominent logo; my name and title; phone number; email address; web address; mentioned "QVL Certified" or similar; should indicate "Aerial visual"
Nice to have
• Watermark of logo or otherwise
Should not have
• Pictures of drones or scenic shots

```html
<!DOCTYPE html>
<html lang="en">
<head>
<meta charset="utf-8">
<title>Skyvant Business Card</title>
<link rel="stylesheet" href="https://fonts.googleapis.com/css2?family=Montserrat:wght@500;600;700;800&display=swap">
<style>
  :root {
    --navy: #233a5e;
    --sky: #1f8fd6;
    --white: #ffffff;
    --mist: #eef2f8;
    --mist-deep: #e1e8f2;
    --stage: #2a2a2c;
  }
  * { box-sizing: border-box; margin: 0; padding: 0; }
  html, body { width: 1200px; height: 852px; overflow: hidden; }
  body {
    background: var(--stage);
    font-family: "Montserrat", sans-serif;
    position: relative;
  }
  .card {
    position: absolute;
    top: 266px;
    width: 540px;
    height: 320px;
    border-radius: 22px;
    overflow: hidden;
    background: var(--white);
  }
  .card--front { left: 45px; }
  .card--back { left: 615px; }

  /* Front */
  .front-pattern {
    position: absolute;
    inset: 0 0 52px 0;
    background: linear-gradient(135deg, var(--mist) 0%, var(--white) 50%, var(--mist-deep) 100%);
  }
  .brand {
    display: flex;
    align-items: center;
    color: var(--navy);
    font-weight: 700;
    letter-spacing: -1px;
    line-height: 1;
    white-space: nowrap;
  }
  .brand__square {
    background: var(--sky);
    display: block;
    flex: none;
  }
  .front-brand {
    position: absolute;
    top: 84px;
    left: 0; right: 0;
    justify-content: center;
    gap: 12px;
    font-size: 72px;
  }
  .front-brand .brand__square { width: 36px; height: 36px; }
  .services {
    position: absolute;
    bottom: 66px;
    left: 0; right: 0;
    text-align: center;
    white-space: nowrap;
    font-size: 11.5px;
    font-weight: 600;
    letter-spacing: 0.5px;
    color: var(--navy);
    text-transform: uppercase;
  }
  .services .dot {
    display: inline-block;
    width: 7px; height: 7px;
    background: var(--sky);
    margin: 0 6px 1px;
  }
  .cert-band {
    position: absolute;
    left: 0; right: 0; bottom: 0;
    height: 52px;
    background: var(--navy);
    color: var(--white);
    display: flex;
    align-items: center;
    justify-content: center;
    white-space: nowrap;
    font-size: 13px;
    font-weight: 600;
    letter-spacing: 1.2px;
    text-transform: uppercase;
  }

  /* Back */
  .contact-panel {
    position: absolute;
    top: 0; bottom: 0; left: 0;
    width: 312px;
    background: var(--navy);
    color: var(--white);
    padding: 70px 0 0 44px;
  }
  .accent-stripe {
    position: absolute;
    top: 0; bottom: 0;
    left: 318px;
    width: 8px;
    background: var(--sky);
  }
  .person__name {
    font-size: 23px;
    font-weight: 800;
    letter-spacing: 0.5px;
    text-transform: uppercase;
    white-space: nowrap;
  }
  .person__title {
    font-size: 14px;
    font-weight: 600;
    color: var(--sky);
    letter-spacing: 0.6px;
    text-transform: uppercase;
    margin-top: 2px;
  }
  .contact-list {
    position: absolute;
    left: 44px;
    bottom: 40px;
    list-style: none;
    font-size: 14px;
    font-weight: 500;
    line-height: 1.55;
    white-space: nowrap;
  }
  .back-brand {
    position: absolute;
    top: 112px;
    left: 326px;
    right: 0;
    justify-content: center;
    gap: 8px;
    font-size: 36px;
  }
  .back-brand .brand__square { width: 18px; height: 18px; }
  .address {
    position: absolute;
    top: 166px;
    left: 326px;
    right: 0;
    text-align: center;
    white-space: nowrap;
    font-size: 12.5px;
    font-weight: 600;
    color: var(--navy);
    line-height: 1.4;
  }
</style>
</head>
<body>
  <section class="card card--front" aria-label="Business card front">
    <div class="front-pattern" role="img" aria-label="Faint light hexagonal pattern background"></div>
    <div class="brand front-brand"><span class="brand__square"></span>skyvant</div>
    <p class="services">Aerial visual for real estate<span class="dot"></span>insurance<span class="dot"></span>construction<span class="dot"></span>film</p>
    <div class="cert-band">QVL Part 107 Commercial sUAS Certified</div>
  </section>

  <section class="card card--back" aria-label="Business card back">
    <div class="contact-panel">
      <h1 class="person__name">Owen Hartley</h1>
      <p class="person__title">Managing Director</p>
      <ul class="contact-list">
        <li>0722-415-390</li>
        <li>owenhartley@nelvo.com</li>
        <li>northfieldmedia.com</li>
      </ul>
    </div>
    <div class="accent-stripe"></div>
    <div class="brand back-brand"><span class="brand__square"></span>skyvant</div>
    <p class="address">2318 Lake Avenue Unit 400<br>Fairmont, Il 60231</p>
  </section>
</body>
</html>
```